Velko's Plumbing, Heating, and AC Buisness card

I need a business card design for my Plumbing Heating and AC company. We are based out of North Windham, CT, and offer residential and light commercial services. I am looking for something that incorporates a water droplet, snowflake, and flame. I would like it to be Modern and different from a typical business card but needs to communicate confidence and security.

```html
<!DOCTYPE html>
<html lang="en">
<head>
<meta charset="utf-8">
<title>Velko's Plumbing, Heating, and AC – Business Card</title>
<link rel="stylesheet" href="https://fonts.googleapis.com/css2?family=Montserrat:wght@500;700;800&family=Arimo:wght@400&display=swap">
<style>
  :root {
    --stage: #2b2b2b;
    --card-dark: #221f20;
    --card-dark-mark: #141213;
    --card-light: #ffffff;
    --ink: #15171a;
    --rule: #9a9a9a;
    --water: #2d8bdc;
    --flame: #cf1c22;
    --frost: #3bbcc2;
  }
  * { margin: 0; padding: 0; box-sizing: border-box; }
  html, body {
    width: 1200px; height: 1040px; overflow: hidden;
    background: var(--stage);
  }
  .stage {
    width: 1200px; height: 1040px;
    display: flex; flex-direction: column; align-items: center; justify-content: center;
    gap: 44px;
  }
  .card {
    width: 760px; height: 434px;
    position: relative;
    box-shadow: 0 14px 30px rgba(0,0,0,.45);
  }
  .card--back {
    background: var(--card-dark);
    border-radius: 90px 0 90px 0;
    display: flex; align-items: center; justify-content: center;
  }
  .card--front {
    background: var(--card-light);
    border-radius: 0 90px 0 90px;
    display: flex; align-items: center;
  }
  .brand {
    display: flex; align-items: center; gap: 22px;
    font-family: "Montserrat", sans-serif; font-weight: 800;
    letter-spacing: -1px;
  }
  .brand__square { width: 64px; height: 64px; border-radius: 6px; }
  .card--back .brand { color: var(--card-dark-mark); font-size: 92px; }
  .card--back .brand__square { background: var(--card-dark-mark); width: 80px; height: 80px; }
  .card--front .brand { color: var(--ink); font-size: 66px; }
  .card--front .brand__square { background: var(--water); }
  .front__logo {
    width: 370px; height: 100%;
    display: flex; align-items: center; justify-content: center;
    padding-left: 20px;
  }
  .front__divider {
    width: 1px; height: 230px; background: var(--rule); opacity: .6;
  }
  .front__details {
    padding-left: 48px;
    font-family: "Arimo", sans-serif; color: var(--ink);
  }
  .person__name {
    font-family: "Montserrat", sans-serif; font-weight: 700;
    font-size: 30px; letter-spacing: .5px; line-height: 1;
  }
  .person__role {
    font-family: "Montserrat", sans-serif; font-weight: 500;
    font-size: 20px; margin: 6px 0 16px;
  }
  .contact { list-style: none; }
  .contact__item {
    display: flex; align-items: center; gap: 10px;
    font-size: 20px; line-height: 30px;
  }
  .contact__icon { width: 22px; height: 20px; flex: none; }
  .address { font-size: 20px; line-height: 25px; margin-top: 16px; }
</style>
</head>
<body>
<main class="stage">
  <section class="card card--back" aria-label="Card back">
    <div class="brand"><span class="brand__square"></span>Velko's</div>
  </section>

  <section class="card card--front" aria-label="Card front">
    <div class="front__logo">
      <div class="brand"><span class="brand__square"></span>Velko's</div>
    </div>
    <div class="front__divider"></div>
    <div class="front__details">
      <p class="person__name">DANIEL REYES</p>
      <p class="person__role">Managing Director</p>
      <ul class="contact">
        <li class="contact__item">
          <svg class="contact__icon" viewBox="0 0 22 20"><rect width="22" height="20" rx="2" fill="var(--water)"/><path d="M7 5c1 0 2 2 2 3s-1 1-1 1.5 2 3 3 3 .5-1 1.5-1 3 1 3 2-1 2-2.5 2C9 15.5 5 11 5 7.5 5 6 6 5 7 5z" fill="#fff"/></svg>
          860-555 014 27
        </li>
        <li class="contact__item">
          <svg class="contact__icon" viewBox="0 0 22 20"><rect width="22" height="20" rx="2" fill="var(--flame)"/><rect x="5" y="6" width="12" height="8" fill="none" stroke="#fff" stroke-width="1.4"/><path d="M5 6l6 5 6-5" fill="none" stroke="#fff" stroke-width="1.4"/></svg>
          info@velkosplumbing.com
        </li>
        <li class="contact__item">
          <svg class="contact__icon" viewBox="0 0 22 20"><rect width="22" height="20" rx="2" fill="var(--frost)"/><g fill="none" stroke="#fff" stroke-width="1.2"><circle cx="11" cy="10" r="5.5"/><ellipse cx="11" cy="10" rx="2.4" ry="5.5"/><path d="M5.5 10h11M6.5 7h9M6.5 13h9"/></g></svg>
          www.velkosplumbing.com
        </li>
      </ul>
      <p class="address">18 Mill Street, North Windham<br>06256, CT, USA</p>
    </div>
  </section>
</main>
</body>
</html>
```